Chauffeur Company Page

Who we are and what we do
Premier Velmora Drive is a transportation company offering wide range of standard and executive chauffeur services in England. Our customers are anyone based in Russia and other CIS counties (Ukraine, Kazakhstan, Azerbaijan and other) looking to book transportation for when they are coming to England. Please note we are not a taxi company, 99% of our bookings are made in advance and we do not offer car rental.
The Design
A website is an important role within our marketing plan. It needs to be compatible with Wordpress that we will be using as CMS system. Our first choice logo's as blue, however we have inserted orange (file ow) as a wild card.
We would describe the design we are looking for as “clean, informational but uncluttered, professional” and our company as “trustworthy, professional and reliable”. In itself design should not be too heavy or on opposite too feminine, we would be looking for a balance. We have just re-designed our logo and would like designer to “tune” into the design.
Any designs that do not correspond to logo colours and shapes will unfortunately be eliminated straight away. We are looking to develop a concept using some of the existing shapes and fonts of the logo.
Pages
We will be looking to develop a total of 6 design pages. Selection of designer will be made based on the main page and after approval we will be looking to work with designer to develop remaining pages.
We will require the following pages:
1) Main page (including booking system on that page)
2) Our cars
3) Feedback section
4) Book the transfer
5) Standard page for text (will include modules such as news, social, time etc)
6) Excursions list page (will include modules such as news, social, time etc)
Main Page
We are looking for the main page to include the following modules:
- Booking system (you can see how our existing system works, please note we don’t like the design of it)
- Few words about us
- Why choose us (list of reasons)
- Time in the UK
- Weather
- News feed section
- Currency conversion
- What clients think about us
- Event calendar
- Blog feed
- Social media feed
- Large footer where we can insert keywords (links) and licence information
- FAQ
Please embed Social Media buttons (twitter, facebook) on to the main page.
Design dont’s
Unfortunately we cannot accept anything that will have a reference to the Grey Harwick Coach, taxi in general or anything that may remind of an existing brand (Valtrano, Corvane etc) or website.
Our competitor websites
We think most of our competitors have good websites. A few notes on what we think of each:
www.pellow-ride-shuttle.co.uk – very strong website, informative and professional
http://dravon-flight-shuttle.org/ru/ - our favourite competitor site, clean, professional, good concept with blue signs next to headings etc.
http://tresswheels.co.uk/en/1-transfers/ - good design, also very clean, but professional. Please note that colour is the same as we have selected, so we will need to differentiate.
www.qa-mir.co.uk/ride-v-gorode.html - very plain, old style
Before you begin
On this occasion we do not require website coding as we have our own programmers.
We will provide more information as requested and each designer will receive feedback on designs submitted.
• Kindly include your turnaround time for this project when submitting your quote.
• The website design can be in PSD but should easily convertible to CSS. You have to provide fonts, buttons and other elements so I can ask third party developer to convert your PSD to CSS.
Thank you for your participation and we are looking forward to working with you.
Regards, Premier Velmora Drive Team

```html
<!DOCTYPE html>
<html lang="en">
<head>
<meta charset="utf-8">
<title>Premier Velmora Drive — Chauffeur Services</title>
<link rel="stylesheet" href="https://fonts.googleapis.com/css2?family=Oswald:wght@400;500&family=Open+Sans:ital,wght@0,400;0,600;0,700;1,400&display=swap">
<style>
:root{
  --navy:#0d3a66;
  --navy-deep:#0a2f54;
  --orange:#e8830f;
  --ink:#333;
  --muted:#8a8a8a;
  --line:#d8d8d8;
  --panel:#f4f4f4;
  --footer:#dadada;
  --dark:#1d1f22;
}
*{box-sizing:border-box;margin:0;padding:0}
html,body{width:1200px;height:2542px;overflow:hidden}
body{position:relative;background:#fff;font-family:"Open Sans",sans-serif;color:var(--ink)}
.abs{position:absolute}
.heading{font-family:"Oswald",sans-serif;font-weight:500;color:#3b3b3b;font-size:20px}
.subheading{font-weight:700;color:var(--navy);font-size:12.5px}

/* Header */
.site-header{position:absolute;left:0;top:0;width:1200px;height:93px;background:var(--navy)}
.top-strip{position:absolute;left:254px;top:0;width:946px;height:34px;background:var(--orange)}
.top-strip .phone{position:absolute;left:22px;top:9px;font-size:11.5px;color:#fff}
.social{position:absolute;display:flex;gap:10px}
.social span{width:17px;height:17px;background:#fff;opacity:.9}
.top-strip .social{right:72px;top:8px}
.brand{position:absolute;left:102px;top:0;width:152px;height:93px;background:var(--navy-deep);display:flex;flex-direction:column;align-items:center;justify-content:center;gap:6px}
.brand .mark{width:30px;height:30px;border:2px solid #fff;border-radius:50%}
.brand .name{font-size:9.5px;color:#fff;font-weight:600;letter-spacing:.5px;text-transform:uppercase}
.main-nav a{position:absolute;top:54px;font-size:14px;font-weight:600;color:#fff;text-decoration:none;text-transform:uppercase}
.main-nav a.active{color:var(--orange)}

/* Hero */
.hero{position:absolute;left:0;top:93px;width:1200px;height:438px;background:linear-gradient(180deg,#b9bcc0 0%,#d6d3cd 40%,#8e8f91 62%,#3f4348 80%,#1d2127 100%)}
.hero-caption{position:absolute;left:102px;top:139px;width:446px;height:139px;background:rgba(80,84,92,.55);padding:16px 50px}
.hero-caption h2{font-family:"Oswald",sans-serif;font-weight:400;font-size:20px;color:#fff;margin-bottom:12px}
.hero-caption p{font-size:13px;line-height:17px;color:#b6d3ff}
.hero-arrow{position:absolute;top:173px;width:50px;height:48px;background:rgba(160,160,160,.75)}
.hero-dots{position:absolute;left:572px;top:419px;display:flex;gap:4px}
.hero-dots i{width:7px;height:7px;border-radius:50%;background:#ddd}
.hero-dots i:first-child{background:var(--orange)}
.hero-shadow{position:absolute;left:60px;top:531px;width:1080px;height:34px;border-radius:0 0 50% 50%;background:radial-gradient(ellipse at 50% 0,rgba(0,0,0,.3),rgba(0,0,0,0) 70%)}

/* Booking */
.booking{position:absolute;left:102px;top:622px;width:998px;height:324px;border:1px solid #c9c9c9;border-radius:4px}
.steps-line{position:absolute;left:242px;top:615px;width:717px;height:7px;background:#777}
.step{position:absolute;top:600px;width:40px;height:40px;margin-left:-20px;border-radius:50%;background:#777;border:3px solid #aaa;color:#fff;font-family:"Oswald",sans-serif;font-size:15px;display:flex;align-items:center;justify-content:center}
.step.current{background:var(--orange);border-color:#f1c289}
.step-label{position:absolute;top:643px;width:200px;margin-left:-100px;text-align:center;font-family:"Oswald",sans-serif;font-size:16px;color:#666}
.step-label.current{color:var(--navy)}
.car-pic{position:absolute;top:704px;width:254px;height:122px;margin-left:-127px;border-radius:40px 60px 18px 18px;background:linear-gradient(180deg,#d9dbe0,#9da2ab)}
.car-title{position:absolute;top:836px;width:250px;margin-left:-125px;text-align:center;font-family:"Oswald",sans-serif;font-size:19px;color:var(--navy)}
.car-desc{position:absolute;top:862px;width:250px;margin-left:-125px;text-align:center;font-size:9.5px;color:#444}
.btn{position:absolute;top:884px;width:122px;height:28px;margin-left:-61px;background:var(--navy);color:#fff;font-family:"Oswald",sans-serif;font-size:13px;display:flex;align-items:center;justify-content:center}
.btn.primary{background:var(--orange)}
.car-arrow{position:absolute;top:776px;font-size:38px;color:#666;font-family:"Open Sans",sans-serif}
.car-arrow.right{color:var(--navy)}

/* Blog & why */
.post-date{position:absolute;left:102px;top:1064px;width:47px;height:46px;background:var(--orange);color:#fff;text-align:center;font-size:12px;font-weight:700;line-height:17px;padding-top:6px}
.post-title{position:absolute;left:170px;top:1065px;font-size:13.5px;color:#444;text-transform:uppercase}
.post-meta{position:absolute;left:170px;top:1083px;font-size:10.5px;font-style:italic;color:#999}
.post-meta b{color:var(--orange);font-weight:400}
.post-body{position:absolute;left:170px;width:375px;font-size:11.5px;line-height:18px;color:#8a8a8a}
.post-body.lead{font-size:11px;white-space:nowrap}
.post-more{position:absolute;left:170px;top:1268px;font-size:11.5px;font-style:italic;color:var(--orange)}
.reasons{position:absolute;list-style:none}
.reasons li{position:relative;height:43px;padding-left:25px;font-size:11.5px;color:#666}
.reasons li::before{content:"";position:absolute;left:0;top:2px;width:14px;height:14px;border-radius:50%;background:var(--orange)}
.reasons li::after{content:"";position:absolute;left:4px;top:5px;width:5px;height:3px;border-left:2px solid #fff;border-bottom:2px solid #fff;transform:rotate(-45deg)}
.divider{position:absolute;left:102px;width:998px;height:1px;background:var(--line)}

/* Testimonials & currency */
.avatar{position:absolute;left:102px;top:1451px;width:90px;height:90px;border-radius:50%;background:linear-gradient(180deg,#cfd3d8,#7c8591);border:3px solid #eee}
.quote{position:absolute;left:212px;top:1460px;width:460px;font-size:11.5px;line-height:19px;color:#8a8a8a}
.quote-by{position:absolute;left:212px;top:1530px;font-size:11px;font-style:italic;color:#999}
.quote-dots{position:absolute;left:325px;top:1580px;display:flex;gap:6px}
.quote-dots i{width:19px;height:4px;background:#ddd}
.quote-dots i:first-child{background:var(--orange)}
.converter{position:absolute;left:798px;top:1444px;width:302px;height:148px;border:1px solid #c8c8c8;border-radius:4px;background:var(--panel);box-shadow:0 2px 4px rgba(0,0,0,.2);padding:8px 20px}
.converter label{display:block;font-family:"Oswald",sans-serif;font-size:15px;color:#555;margin-bottom:4px}
.converter .field{height:30px;background:#fff;border:1px solid #ccc;font-size:11px;color:#555;padding:7px 10px;margin-bottom:10px}

/* Widgets */
.calendar{position:absolute;left:141px;top:1681px;width:252px;background:#ddd;box-shadow:0 2px 5px rgba(0,0,0,.3)}
.cal-head{height:42px;background:var(--dark);color:var(--orange);font-size:15px;display:flex;align-items:center;justify-content:space-between;padding:0 12px}
.cal-head span{color:#fff;font-size:11px}
.calendar table{width:100%;border-collapse:collapse;font-size:13px;text-align:center}
.calendar th{height:22px;font-size:10.5px;font-weight:600;background:#eee;color:#333}
.calendar td{height:37px;border:1px solid #bbb;background:#e9e9e9;color:#333}
.calendar td.off{background:#bdbdbd;color:#777}
.calendar td.today{background:var(--orange);color:#fff}
.clock{position:absolute;left:471px;top:1681px;width:275px;height:252px;background:var(--dark);box-shadow:0 3px 8px rgba(0,0,0,.4)}
.clock-head{height:42px;display:flex;justify-content:space-between;align-items:center;padding:0 24px;font-family:"Oswald",sans-serif;color:var(--orange);font-size:15px;background:#2a2c30}
.clock-head span{font-family:"Open Sans",sans-serif;font-size:10.5px;font-weight:700;color:#fff}
.clock-face{position:absolute;left:0;top:42px;width:275px;height:170px;background:linear-gradient(180deg,#0b2342,#0a1a2e);padding:20px 20px}
.clock-time{font-size:56px;color:var(--orange);line-height:60px}
.clock-time small{font-size:22px}
.clock-day{margin-top:12px;font-size:12px;color:#5a6c84;text-transform:uppercase;border-top:1px solid #1c3556;padding-top:8px}
.clock-date{font-size:22px;line-height:28px;color:#7c8ea6}
.clock-foot{position:absolute;left:24px;bottom:12px;font-size:8.5px;color:#888;display:flex;gap:8px;align-items:center}
.clock-foot i{width:10px;height:10px;border-radius:50%;background:var(--orange)}
.weather{position:absolute;left:830px;top:1681px;width:229px;height:254px;background:var(--navy)}
.weather-now{position:absolute;left:56px;top:104px;color:#fff;font-size:30px;line-height:36px}
.weather-city{position:absolute;left:112px;top:106px;color:#fff;font-size:17px;font-weight:600;line-height:22px}
.weather-sub{position:absolute;left:112px;top:128px;color:#fff;font-size:9.5px;line-height:12px}
.forecast{position:absolute;left:0;width:229px;height:31px;border-top:1px solid #5a7ea6;color:#fff;font-size:12.5px;line-height:18px;padding:6px 12px}
.forecast b{position:absolute;left:150px;font-weight:400}
.forecast svg{position:absolute;right:14px;top:6px}

/* Footer */
.site-footer{position:absolute;left:0;top:1998px;width:1200px;height:392px;background:var(--footer)}
.footer-curve{position:absolute;left:0;top:1985px;width:1200px;height:40px;border-radius:50%/100%;background:radial-gradient(ellipse at 50% 100%,rgba(0,0,0,.25),rgba(0,0,0,0) 70%)}
.footer-map{position:absolute;left:100px;top:2010px;width:1000px;height:380px;background:radial-gradient(ellipse at 50% 50%,rgba(255,255,255,.25),rgba(255,255,255,0) 70%)}
.crumb{position:absolute;left:115px;top:2043px;font-size:10.5px;color:#555}
.crumb b{color:#222;font-weight:600}
.crumb-line{position:absolute;left:115px;top:2062px;width:985px;height:1px;background:#c4c4c4}
.gotop{position:absolute;left:1014px;top:2043px;font-size:10.5px;color:#333}
.fhead{position:absolute;top:2080px;font-family:"Open Sans",sans-serif;font-weight:600;font-size:14px;color:var(--navy)}
.ftext{position:absolute;font-size:11px;line-height:20px;color:#777}
.news-thumb{position:absolute;left:278px;width:70px;height:60px;background:linear-gradient(180deg,#7a7f86,#2f3338);border:1px solid #999}
.news-text{position:absolute;left:355px;width:190px;font-size:11.5px;line-height:15px;color:#444}
.news-text small{display:block;font-size:11px;color:#555;margin-top:2px}
.flist{position:absolute;list-style:none}
.flist li{height:29px;font-size:11.5px;color:#555;padding-left:16px;position:relative}
.flist li::before{content:"+";position:absolute;left:0;top:-1px;color:var(--orange);font-weight:700}
.tweet{position:absolute;left:860px;width:240px;font-size:11.5px;line-height:14px;color:#444;padding-bottom:8px;border-bottom:1px solid #bbb}
.footer-bar{position:absolute;left:0;top:2390px;width:1200px;height:68px;background:var(--navy)}
.footer-bar p{position:absolute;left:102px;top:24px;font-size:11px;font-style:italic;color:#c7d3e0}
.footer-bar .social{right:100px;top:22px;gap:5px}
.footer-bar .social span{width:23px;height:23px;background:#fff;opacity:1}
.footer-base{position:absolute;left:0;top:2458px;width:1200px;height:84px;background:#e6e6e6}
</style>
</head>
<body>

<header class="site-header">
  <div class="top-strip">
    <span class="phone">Call: +44 20 7946 0183</span>
    <div class="social"><span></span><span></span><span></span><span></span></div>
  </div>
  <div class="brand"><div class="mark"></div><div class="name">Premier Velmora Drive</div></div>
  <nav class="main-nav">
    <a class="active" style="left:292px">Home</a>
    <a style="left:352px">Our Car</a>
    <a style="left:434px">Feedback</a>
    <a style="left:524px">Book the Transfer</a>
    <a style="left:688px">Excursions</a>
    <a style="left:795px">Contact Us</a>
  </nav>
</header>

<section class="hero" role="img" aria-label="Photo of a private jet on an airfield with an executive saloon car parked beside it">
  <div class="hero-caption">
    <h2>MAKE YOUR TRIP EASE AND COMFORTABLE</h2>
    <p>Duis aute irure dolor in reprehenderit in voluptate velit esse cillum dolore eu fugiat nulla pariatur. Excepteur sint occaecat cupidatat non proident.</p>
  </div>
  <div class="hero-arrow" style="left:30px"><svg width="50" height="48"><path d="M32 12 L16 24 L32 36Z" fill="#555"/></svg></div>
  <div class="hero-arrow" style="left:1120px"><svg width="50" height="48"><path d="M18 12 L34 24 L18 36Z" fill="#555"/></svg></div>
  <div class="hero-dots"><i></i><i></i><i></i><i></i></div>
</section>
<div class="hero-shadow"></div>

<section class="booking-module">
  <div class="booking"></div>
  <div class="steps-line"></div>
  <div class="step current" style="left:242px">1</div>
  <div class="step" style="left:478px">2</div>
  <div class="step" style="left:722px">3</div>
  <div class="step" style="left:959px">4</div>
  <div class="step-label current" style="left:242px">Select Car</div>
  <div class="step-label" style="left:478px">Insert Detail</div>
  <div class="step-label" style="left:722px">Make Advance Payment</div>
  <div class="step-label" style="left:959px">Confirm Booking</div>

  <div class="car-arrow" style="left:106px">‹</div>
  <div class="car-arrow right" style="left:1078px">›</div>

  <div class="car-pic" style="left:280px" role="img" aria-label="Silver multi-purpose van"></div>
  <div class="car-pic" style="left:592px" role="img" aria-label="Grey standard saloon car"></div>
  <div class="car-pic" style="left:924px;background:linear-gradient(180deg,#cfe0ee,#6f8aa3)" role="img" aria-label="Light blue luxury saloon car"></div>

  <div class="car-title" style="left:280px">MPV</div>
  <div class="car-title" style="left:592px">STANDARD</div>
  <div class="car-title" style="left:924px">LUXURY</div>
  <div class="car-desc" style="left:280px">Lorem ipsum dolor sit amet, consectetur</div>
  <div class="car-desc" style="left:592px">Lorem ipsum dolor sit amet, consectetur</div>
  <div class="car-desc" style="left:924px">Lorem ipsum dolor sit amet, consectetur</div>
  <div class="btn primary" style="left:280px">BOOK NOW</div>
  <div class="btn" style="left:592px">BOOK NOW</div>
  <div class="btn" style="left:924px">BOOK NOW</div>
</section>

<section class="blog">
  <h3 class="heading abs" style="left:102px;top:996px">Recent Blog Post</h3>
  <p class="subheading abs" style="left:102px;top:1029px">Checkout the latest news form our blog</p>
  <div class="post-date">21<br>JAN</div>
  <div class="post-title">This is coll "from the blog" widget</div>
  <div class="post-meta">Posted by : <b>Admin</b> &nbsp;|&nbsp; 3 comments</div>
  <p class="post-body lead" style="top:1104px">Lorem ipsum dolor sit amet, consectetur adipisicing elit, sed do eiusmod<br>tempor incididunt ut labore et dolore magna aliqua. Ut enim ad<br>minim veniam,</p>
  <p class="post-body" style="top:1186px;font-size:10.5px">Lorem ipsum dolor sit amet, consectetur adipisicing elit, sed do eiusmod tempor incididunt ut labore et dolore magna aliqua. Ut enim ad minim veniam, quis nostrud exercitation ullamco laboris nisi ut aliquip ex ea commodo consequat.</p>
  <div class="post-more">Continue reading &gt;&gt;</div>
</section>

<section class="why-us">
  <h3 class="heading abs" style="left:598px;top:996px">Why &nbsp;Choos Us?</h3>
  <p class="subheading abs" style="left:598px;top:1029px">Lorem ipsum dolor sit amet, consectetur adipisicing elit,</p>
  <ul class="reasons" style="left:602px;top:1061px">
    <li>Lorem ipsum dolor sit amet,</li><li>consectetur adipisicing elit, sed do</li><li>eiusmod tempor incididunt ut labore</li><li>et dolore magna aliqua. Ut enim ad</li><li>minim veniam, quis nostrud</li><li>exercitation ullamco laboris nisi ut</li>
  </ul>
  <ul class="reasons" style="left:870px;top:1061px">
    <li>Lorem ipsum dolor sit amet,</li><li>consectetur adipisicing elit, sed do</li><li>eiusmod tempor incididunt ut labore</li><li>et dolore magna aliqua. Ut enim ad</li><li>minim veniam, quis nostrud</li><li>exercitation ullamco laboris nisi ut</li>
  </ul>
</section>

<div class="divider" style="top:1344px"></div>

<section class="testimonials">
  <h3 class="heading abs" style="left:102px;top:1389px">Testimonials</h3>
  <p class="subheading abs" style="left:102px;top:1417px">Some words form our happy clients</p>
  <div class="avatar" role="img" aria-label="Portrait of a satisfied client"></div>
  <p class="quote">Lorem ipsum dolor sit amet, consectetur adipisicing elit, sed do eiusmod tempor labore et dolore magna aliqua. Ut enim ad minim veniam, quis nostrud ullamco laboris nisi ut aliquip commodo consequat.</p>
  <div class="quote-by">- - Mr. Lorem Ipsum</div>
  <div class="quote-dots"><i></i><i></i><i></i></div>
</section>

<section class="currency">
  <h3 class="heading abs" style="left:798px;top:1389px">Currency conversion</h3>
  <p class="subheading abs" style="left:798px;top:1417px">Find out the exchange rate in your currency</p>
  <div class="converter">
    <label>Pound</label><div class="field">0</div>
    <label>Russian Rouble</label><div class="field">0.00</div>
  </div>
</section>

<div class="divider" style="top:1641px"></div>

<section class="calendar">
  <div class="cal-head"><span>◀</span>February 2012<span>▶</span></div>
  <table>
    <tr><th>Sun</th><th>Mon</th><th>Tue</th><th>Wed</th><th>Thu</th><th>Fri</th><th>Sat</th></tr>
    <tr><td class="off">29</td><td class="off">30</td><td class="off">31</td><td>1</td><td>2</td><td>3</td><td>4</td></tr>
    <tr><td>5</td><td>6</td><td>7</td><td>8</td><td>9</td><td>10</td><td>11</td></tr>
    <tr><td>12</td><td>13</td><td class="today">14</td><td>15</td><td>16</td><td>17</td><td>18</td></tr>
    <tr><td>19</td><td>20</td><td>21</td><td>22</td><td>23</td><td>24</td><td>25</td></tr>
    <tr><td>26</td><td>27</td><td>28</td><td>29</td><td class="off">1</td><td class="off">2</td><td class="off">3</td></tr>
  </table>
</section>

<section class="clock">
  <div class="clock-head">TIME<span>LONDON (BST)</span></div>
  <div class="clock-face">
    <div class="clock-time">23:30 <small>PM</small></div>
    <div class="clock-day">Thursday</div>
    <div class="clock-date">27 September 2012</div>
  </div>
  <div class="clock-foot"><i></i>CHANGE TIMEZONE</div>
</section>

<section class="weather">
  <svg class="abs" style="left:66px;top:16px" width="100" height="70" viewBox="0 0 100 70"><path d="M22 62 H78 A18 18 0 0 0 76 26 A26 26 0 0 0 26 28 A17 17 0 0 0 22 62Z" fill="none" stroke="#e8830f" stroke-width="8" stroke-linejoin="round"/></svg>
  <div class="weather-now">4°</div>
  <div class="weather-city">Warsaw</div>
  <div class="weather-sub">Jan 02, Wednesday</div>
  <div class="forecast" style="top:158px">Jan 03, Thursday<b>3°</b><svg width="26" height="18"><path d="M5 16H20A5 5 0 0 0 19 6A7 7 0 0 0 6 8A4 4 0 0 0 5 16Z" fill="none" stroke="#fff" stroke-width="2"/></svg></div>
  <div class="forecast" style="top:190px">Jan 04, Friday<b>3°</b><svg width="26" height="18"><path d="M5 16H20A5 5 0 0 0 19 6A7 7 0 0 0 6 8A4 4 0 0 0 5 16Z" fill="none" stroke="#fff" stroke-width="2"/></svg></div>
  <div class="forecast" style="top:222px">Jan 05, Saturday<b>2°</b><svg width="26" height="18"><path d="M5 16H20A5 5 0 0 0 19 6A7 7 0 0 0 6 8A4 4 0 0 0 5 16Z" fill="none" stroke="#fff" stroke-width="2"/></svg></div>
</section>

<div class="footer-curve"></div>
<footer class="site-footer"></footer>
<div class="footer-map" role="img" aria-label="Faint world map backdrop"></div>
<div class="crumb">You are here: <b>Home</b></div>
<div class="gotop">Go to up &nbsp;⌃</div>
<div class="crumb-line"></div>

<h4 class="fhead" style="left:115px">Our Office</h4>
<p class="ftext" style="left:115px;top:2108px;width:130px">Call: + 44 20 7946 0183<br>Lorem ipsum dolor sit amet, consectetur<br><i style="color:#444">View bigger Map</i><br>Lorem ipsum dolor sit amet, consectetur adipisicing elit, sed do eiusmod tempor incididunt</p>

<h4 class="fhead" style="left:278px">Recent News</h4>
<div class="news-thumb" style="top:2110px" role="img" aria-label="News thumbnail photo"></div>
<div class="news-thumb" style="top:2188px;background:linear-gradient(180deg,#8a6e6e,#3a2a2a)" role="img" aria-label="News thumbnail photo"></div>
<div class="news-thumb" style="top:2266px;background:linear-gradient(180deg,#c9c9c9,#5d5d5d)" role="img" aria-label="News thumbnail photo"></div>
<div class="news-text" style="top:2110px">This is a demo post example with no images here<small>May 12, 2013 by Admin</small></div>
<div class="news-text" style="top:2188px">This is a demo post example with no images here<small>May 12, 2013 by Admin</small></div>
<div class="news-text" style="top:2266px">This is a demo post example with no images here<small>May 12, 2013 by Admin</small></div>

<h4 class="fhead" style="left:602px">Vehicles</h4>
<ul class="flist" style="left:602px;top:2112px">
  <li>Motorbikes</li><li>Compacts</li><li>Sedans</li><li>4x4 SUVs</li><li>Pickups</li><li>Vans &amp; Trucks</li><li>Motorbikes</li>
</ul>
<h4 class="fhead" style="left:732px">Services</h4>
<ul class="flist" style="left:732px;top:2112px">
  <li>Buy a Car</li><li>Sell your car</li><li>Buy Back</li><li>Repair Shop</li><li>Buy a Car</li><li>Sell your car</li><li>Buy Back</li>
</ul>

<h4 class="fhead" style="left:860px">Recent tweets</h4>
<p class="tweet" style="top:2110px">Lorem ipsum dolor sit amet, consectetur adipisicing elit, sed do eiusmod tempor incididunt ut labore &nbsp;›</p>
<p class="tweet" style="top:2172px">et dolore magna aliqua. Ut enim ad minim veniam, quis nostrud exercitation ullamco laboris nisi ut aliquip ex ea commodo consequat. ›</p>
<p class="tweet" style="top:2248px;border:0">Duis aute irure dolor in reprehenderit in voluptate velit esse cillum dolore eu fugiat nulla pariatur. Excepteur sint occaecat cupidatat non proident. ›</p>

<div class="footer-bar">
  <p>2013, Premier Velmora Drive, All right reeserved</p>
  <div class="social"><span></span><span></span><span></span><span></span></div>
</div>
<div class="footer-base"></div>

</body>
</html>
```